CD front and back cover and CD disk. Front includes design elements of the attached band photo, the name of the band (Quiet Harbor Lanterns) and the album name (Paper Anchors?). I've attached a photshoped band photo and an original image. I like the color palette of the photoshoped pix but it may be too dark. So I've attached the original pix, that could be photoshoped. Music is alternative rock. See website qhlTunes.com and the EPK on the site. Songs are not up for this CD yet. Concept - modern, clean, NO gothic rock font or style of any kind.

Back cover needs songs, website and contact as follows:

Hold Ember (Electric)
Linger
Bent and Broken
Meridian
You Sink You Swim
Lean Past You
Hold Ember (Acoustic)
Room To Roam
The Tide
Push Too Far

qhlTunes.com
info@qhlTunes.com
- the actual cd needs the same as above
- use the DiscNook template Sleeve S240 

• Back cover needs the song titles, website, contact info and copyright as follows:
Hold Ember (electric)
Linger
Bent and Broken
Meridian
You Sink You Swim
Lean Past You
Hold Ember (acoustic)
Room To Roam
The Tide
Push Too Far

qhlTune.com
info@qhlTunes.com
Copyright © 2013 Quiet Harbor Lanterns | All Rights Reserved
Also - dimensions for CD Sleeve S240 on discnook.com
Also - CD disk to contain all of the above

```html
<!DOCTYPE html>
<html lang="en">
<head>
<meta charset="utf-8">
<title>Quiet Harbor Lanterns – Paper Anchors? Sleeve</title>
<link rel="stylesheet" href="https://fonts.googleapis.com/css2?family=Saira+Semi+Condensed:wght@500;600&display=swap">
<style>
  :root {
    --page-bg: #eef0f1;
    --sleeve-dark: #1f201d;
    --sleeve-mid: #34362f;
    --sleeve-edge: #141512;
    --track-text: #b9c3c2;
    --track-number: #8d9796;
    --contact-text: #6f7573;
    --title-mint: #a9cbbd;
    --band-text: #d3dedb;
    --ember: rgba(196, 74, 22, 0.2);
    --photo-light: #6c7d86;
    --photo-dark: #1c2226;
  }
  * { box-sizing: border-box; margin: 0; padding: 0; }
  html, body {
    width: 1200px; height: 1000px; overflow: hidden;
    background: radial-gradient(ellipse at 50% 40%, #f8f9fa 0%, var(--page-bg) 70%);
    font-family: "Saira Semi Condensed", sans-serif;
  }
  .sleeve-spread {
    position: absolute; left: 160px; top: 86px;
    width: 888px; height: 452px;
  }
  .panel {
    position: absolute; overflow: hidden;
    background:
      radial-gradient(ellipse at 30% 25%, rgba(90,94,82,0.35), transparent 60%),
      radial-gradient(ellipse at 75% 80%, rgba(10,10,8,0.5), transparent 65%),
      linear-gradient(160deg, var(--sleeve-mid), var(--sleeve-dark));
    box-shadow: 0 4px 10px rgba(0,0,0,0.35);
  }
  .back-cover { left: 0; top: 6px; width: 445px; height: 440px; }
  .back-cover::before {
    content: ""; position: absolute; inset: 0;
    background:
      radial-gradient(circle at 22% 70%, var(--ember), transparent 28%),
      radial-gradient(circle at 85% 45%, var(--ember), transparent 22%),
      radial-gradient(circle at 45% 92%, var(--ember), transparent 26%);
  }
  .front-cover { left: 445px; top: 0; width: 443px; height: 452px; border-left: 1px solid var(--sleeve-edge); }

  .track-list {
    position: absolute; top: 118px; left: 0; width: 445px;
    list-style: none; text-align: center;
    font-variant: small-caps; font-weight: 600;
    font-size: 21px; letter-spacing: 1.6px; line-height: 20.7px;
    color: var(--track-text); white-space: nowrap;
  }
  .track-number { color: var(--track-number); font-size: 16px; margin-right: 5px; }
  .contact {
    position: absolute; left: 40px; top: 370px;
    font-variant: small-caps; font-weight: 500;
    font-size: 14px; line-height: 15px; letter-spacing: 1.2px;
    color: var(--contact-text); white-space: nowrap;
  }

  .band-photo { position: absolute; left: 62px; top: 52px; width: 350px; height: 296px; }
  .band-name {
    position: absolute; top: 108px; left: 100px; width: 280px;
    text-align: center; font-variant: small-caps; font-weight: 600;
    font-size: 22px; letter-spacing: 1.6px; color: var(--band-text);
    white-space: nowrap; z-index: 2;
  }
  .album-title {
    position: absolute; top: 362px; left: 78px; width: 335px;
    text-align: center; font-variant: small-caps; font-weight: 600;
    font-size: 33px; letter-spacing: 2.5px; color: var(--title-mint);
    white-space: nowrap;
  }
</style>
</head>
<body>
  <main class="sleeve-spread">
    <section class="panel back-cover">
      <ol class="track-list">
        <li><span class="track-number">01.</span>Hold Ember (Electric)</li>
        <li><span class="track-number">02.</span>Linger</li>
        <li><span class="track-number">03.</span>Bent and Broken</li>
        <li><span class="track-number">04.</span>Meridian</li>
        <li><span class="track-number">05.</span>You Sink You Swim</li>
        <li><span class="track-number">06.</span>Lean Past You</li>
        <li><span class="track-number">07.</span>Hold Ember (Acoustic)</li>
        <li><span class="track-number">08.</span>Room To Roam</li>
        <li><span class="track-number">09.</span>The Tide</li>
        <li><span class="track-number">10.</span>Push Too Far</li>
      </ol>
      <p class="contact">qhlTunes.com<br>info@qhlTunes.com</p>
    </section>

    <section class="panel front-cover">
      <svg class="band-photo" viewBox="0 0 350 296" role="img" aria-label="Band photo: four members standing in dim bluish light, framed by a torn wall opening">
        <defs>
          <radialGradient id="photo-glow" cx="58%" cy="55%" r="60%">
            <stop offset="0%" stop-color="var(--photo-light)"/>
            <stop offset="100%" stop-color="var(--photo-dark)"/>
          </radialGradient>
        </defs>
        <path d="M40 70 L80 46 L120 54 L150 30 L190 44 L222 10 L262 36 L300 52 L330 100 L324 150 L344 196 L318 236 L326 270 L270 286 L210 276 L160 292 L110 280 L60 290 L36 250 L22 200 L32 150 L10 112 Z"
              fill="url(#photo-glow)" stroke="#0e0f0d" stroke-width="3"/>
      </svg>
      <h1 class="band-name">Quiet Harbor Lanterns</h1>
      <h2 class="album-title">Paper Anchors?</h2>
    </section>
  </main>
</body>
</html>
```